Marketing Flyer for Coaching Company

Need a marketing flyer I can use based off of my website Quintelcoaching.com. Quick Summary of me include "over 40,000 hours of leadership and coaching experience" Talking about the three services offered. Career and life coaching / Open Harbor Hotline / Fractional Sales Leadership. I would love to use the colors from the logo. I do not want pricing included.

Target Market(s)

Therapist Offices and other professional treatment centers

Industry/Entity Type

Coaching

Other font styles liked:
• Hero Light Regular

Colors
0054AA
0677BA
7BADD7
CADEEF
E8F1F8
0094D4
00A9DD
6FCCEA
C7EBF8
E9F6FB
00AB8E
00BBA5
67D7C9
C6EFE9
E9F9F6
59FF00
82FF00
B8FF75
E3FFCB
F4FFEA
FFF300
FFF600
FEFA6F
FFFEC7
FFFEE8
EB3D1F
EC4F4E
F09395
F8D3D4
FCEDEE
E54698
E96AAD
F1A4CE
F9D9EA
FCEFF6
A7469A
B969AE
D3A5CF
EDDBEB
F8F0F9
6B429C
8869AF
B7A5CE
E3DAEB
F3F0F8

Requirements
Must have
• Logo "over 40,000 hours of leadership and coaching experience" Talking about the three services offered. Career and life coaching / Open Harbor Hotline / Fractional Sales Leadership. I would love to use the colors from the logo. Contact info
Nice to have
• Color Pallet based off of logo pallet id's are in the attachments
Should not have
• Pricing

```html
<!DOCTYPE html>
<html lang="en">
<head>
<meta charset="utf-8">
<title>Quintel Coaching – Services Flyer</title>
<link rel="stylesheet" href="https://fonts.googleapis.com/css2?family=Lato:ital,wght@0,400;0,700;0,900;1,400;1,700;1,900&display=swap">
<style>
  :root {
    --backdrop: #8a8a8a;
    --paper: #ffffff;
    --ink: #1f2a44;
    --magenta: #b3246c;
    --magenta-deep: #9c1f5e;
    --purple: #5b2d8c;
    --violet: #8a2a99;
    --plum: #6c2e90;
    --pink-soft: #e7a6c7;
    --pink-mid: #c9407f;
    --text-light: #ffffff;
  }
  * { box-sizing: border-box; margin: 0; padding: 0; }
  html, body { width: 1200px; height: 1200px; overflow: hidden; }
  body { background: var(--backdrop); font-family: "Lato", Arial, sans-serif; position: relative; }

  .flyer {
    position: absolute; left: 220px; top: 62px;
    width: 760px; height: 1076px;
    background: var(--paper); overflow: hidden;
  }
  .top-waves { position: absolute; left: 0; top: 0; width: 760px; height: 210px; }

  .brand {
    position: absolute; top: 118px; left: 0; width: 100%;
    display: flex; justify-content: center; align-items: center; gap: 14px;
  }
  .brand-dot { width: 30px; height: 30px; border-radius: 50%; background: var(--purple); }
  .brand-name { font-size: 42px; font-weight: 400; color: var(--ink); letter-spacing: 0.5px; }

  .tagline {
    position: absolute; top: 222px; width: 100%; text-align: center;
    font-style: italic; font-weight: 700; font-size: 24px; color: var(--ink);
  }
  .tagline strong { color: var(--purple); font-weight: 900; font-size: 27px; }

  .footer-band {
    position: absolute; left: 0; top: 787px; width: 100%; height: 289px;
    background: linear-gradient(100deg, var(--plum) 0%, #8a2a8f 55%, var(--magenta) 100%);
  }

  .services { position: absolute; top: 298px; left: 27px; display: flex; gap: 9px; }
  .service { width: 229px; display: flex; flex-direction: column; align-items: stretch; }
  .service-card {
    height: 565px; border-radius: 6px 74px 74px 6px; overflow: hidden;
    box-shadow: 0 6px 12px rgba(0,0,0,0.3);
    display: flex; flex-direction: column;
  }
  .service-head {
    height: 202px; border-radius: 0 74px 0 74px;
    display: flex; align-items: center; justify-content: center; text-align: center;
    padding: 0 14px 58px;
    color: var(--text-light); font-weight: 900; font-size: 25px; line-height: 1.2;
    border-bottom: 3px solid rgba(255,255,255,0.95);
    box-shadow: 0 5px 8px rgba(0,0,0,0.25);
    position: relative; z-index: 1;
  }
  .service-body {
    flex: 1; padding: 38px 18px 20px; margin-top: -2px;
    color: var(--text-light); font-size: 12.6px; line-height: 1.38; text-align: center;
  }
  .service-body p + p { margin-top: 16px; }
  .service-rule { height: 4px; background: var(--paper); margin-top: 27px; }

  .service--career .service-head { background: var(--magenta); }
  .service--career .service-card { background: linear-gradient(180deg, #a22d8a 0%, #8a2d92 100%); }
  .service--hotline .service-head { background: var(--purple); }
  .service--hotline .service-card { background: linear-gradient(180deg, #a22a7c 0%, var(--magenta-deep) 100%); }
  .service--company .service-head { background: var(--violet); }
  .service--company .service-card { background: linear-gradient(180deg, #7a2c95 0%, var(--plum) 100%); }

  .contact {
    position: absolute; top: 972px; width: 100%;
    display: flex; justify-content: center; align-items: center; gap: 24px;
    color: var(--text-light); font-weight: 900; font-size: 46px; letter-spacing: 0.5px;
  }
  .contact-icon { width: 64px; height: 64px; }
</style>
</head>
<body>
  <main class="flyer">
    <svg class="top-waves" viewBox="0 0 760 210" aria-hidden="true">
      <path d="M0 0 H760 V40 C600 20 420 10 260 40 C160 58 70 80 0 110 Z" fill="#f3c9dd"/>
      <path d="M0 0 H760 V18 C560 0 360 -4 200 28 C120 44 50 62 0 80 Z" fill="var(--pink-soft)"/>
      <path d="M0 88 C120 40 300 6 470 10 C560 12 640 30 700 60 C730 76 750 96 760 120 L760 135 C740 100 700 72 640 52 C560 26 420 18 300 34 C180 50 80 80 0 112 Z" fill="var(--pink-mid)"/>
      <path d="M420 18 C560 30 660 80 760 190 L760 160 C690 80 590 34 420 18 Z" fill="#d87aa8"/>
      <path d="M560 0 C650 50 710 110 760 170 L760 200 C700 130 640 70 540 0 Z" fill="var(--magenta)"/>
    </svg>

    <div class="brand">
      <span class="brand-dot"></span>
      <span class="brand-name">Quintel Coaching</span>
    </div>

    <p class="tagline">Over <strong>40,000</strong> hours of leadership and coaching experience.</p>

    <div class="footer-band"></div>

    <section class="services">
      <article class="service service--career">
        <div class="service-card">
          <h2 class="service-head">CAREER<br>COACHING</h2>
          <div class="service-body">
            <p>Sometimes the work isn't about your job—it's about you. I help leaders at all levels develop the confidence, communication skills, and clarity to show up as their best selves, both professionally and personally.</p>
            <p>-or-</p>
            <p>Thinking about a major career change? Feeling stuck and ready for something new? I guide professionals through pivotal transitions with the wisdom of someone who's made bold moves himself—and thrived.</p>
          </div>
        </div>
        <div class="service-rule"></div>
      </article>

      <article class="service service--hotline">
        <div class="service-card">
          <h2 class="service-head">PROFESSIONAL<br>OPEN HARBOR<br>HOTLINE</h2>
          <div class="service-body">
            <p>Remember that friend who always seems to know what to say when you're stuck? That's what this is.</p>
            <p>Sometimes you don't need a six-month coaching program—you just need someone to talk through one specific challenge.</p>
            <p>No long-term commitment. No pressure. Just honest conversation and the kind of guidance you'd get from someone who genuinely cares about seeing you succeed.</p>
          </div>
        </div>
        <div class="service-rule"></div>
      </article>

      <article class="service service--company">
        <div class="service-card">
          <h2 class="service-head">COMPANY<br>SUPPORT</h2>
          <div class="service-body">
            <p>Need senior sales leadership without the full-time commitment? I can step in as your fractional Sales Director, bringing two decades of proven leadership to scale your sales operation, mentor your team, and drive sustainable growth.</p>
            <p>-or-</p>
            <p>Whether you're building a sales team from scratch or refining your approach, my workshops blend strategic insight with relationship-based selling principles that actually work in today's market.</p>
          </div>
        </div>
        <div class="service-rule"></div>
      </article>
    </section>

    <div class="contact">
      <svg class="contact-icon" viewBox="0 0 64 64" aria-hidden="true">
        <circle cx="32" cy="32" r="28" fill="none" stroke="#fff" stroke-width="4"/>
        <path d="M22 17 l6 -1 l4 9 l-4 4 c2 5 6 9 11 11 l4 -4 l9 4 l-1 6 c-1 3 -4 4 -7 3 c-13 -3 -23 -13 -26 -26 c-1 -3 1 -6 4 -6 Z" fill="#fff"/>
        <path d="M36 20 a10 10 0 0 1 8 8 M36 14 a16 16 0 0 1 14 14" fill="none" stroke="#fff" stroke-width="2.5" stroke-linecap="round"/>
      </svg>
      <span class="contact-phone">314-555-0187</span>
    </div>
  </main>
</body>
</html>
```